Polish brewery needs BEER LABEL design for WEDDINGS

We need beer label design for weddings. Our brewery is located on South of Poland and it is called Wytwórnia Orlik [PL]/Factory Falcon [ENG]. We feel strong connection to mountains and we use water from the mountain in our vicinity.
Regarding beer style it is India Pale Ale so beer is bitter and aromatic because of high addition of hops. Label design has to be modern and simple. We would prefer bright and cream colors.
We need to have opportunity to edit data which are on the label so we will need to get appropriate files.
In attached files you can find all details. If any additional information will be required please do not hesitate and contact with me.

Target Market(s)

Weddings

Font styles to use
Sans Serif
Script

Colors
ffffff

Requirements
Must have
• Information listed in documents in attached files
Nice to have
• Some nice graphics
Bright and cream colors.
Should not have
• -

```html
<!DOCTYPE html>
<html lang="pl">
<head>
<meta charset="utf-8">
<title>Etykieta weselna – India Pale Ale</title>
<link rel="stylesheet" href="https://fonts.googleapis.com/css2?family=Open+Sans:wght@400;600;700&family=Great+Vibes&family=Kaushan+Script&display=swap">
<style>
  :root {
    --page: #ffffff;
    --cream: #fdf3e4;
    --brown: #6b4a2e;
    --text: #3e2a1a;
    --leaf: #cbb896;
    --leaf-soft: #e9dcc5;
    --leaf-faint: #f4e9d8;
    --line: #c9b591;
  }
  html, body { margin: 0; padding: 0; }
  body {
    width: 1025px; height: 1200px; overflow: hidden;
    background: var(--page);
    font-family: "Open Sans", Arial, sans-serif;
    color: var(--text);
    position: relative;
  }
  .label {
    position: absolute; left: 20px; top: 393px;
    width: 985px; height: 414px;
    background: var(--cream);
    border-radius: 14px;
    overflow: hidden;
  }
  .art { position: absolute; border-radius: 10px; }
  .wreath-arcs { position: absolute; left: 0; top: 0; width: 985px; height: 414px; }
  .leaves-left {
    left: 304px; top: 120px; width: 96px; height: 146px;
    background: linear-gradient(160deg, var(--leaf-soft), var(--leaf));
    opacity: .55;
  }
  .leaves-right {
    left: 594px; top: 50px; width: 62px; height: 128px;
    background: linear-gradient(200deg, var(--leaf-soft), var(--leaf));
    opacity: .55;
  }
  .sprig-left {
    left: 14px; top: 204px; width: 76px; height: 200px;
    background: linear-gradient(180deg, var(--leaf-faint), transparent);
  }
  .sprig-right {
    left: 872px; top: 204px; width: 82px; height: 200px;
    background: linear-gradient(180deg, var(--leaf-faint), transparent);
  }
  .couple {
    left: 422px; top: 215px; width: 132px; height: 164px;
    background: linear-gradient(180deg, #e3d4ba 0%, #cdb994 100%);
  }
  .info { position: absolute; font-size: 12.5px; line-height: 17.5px; margin: 0; }
  .info b { font-weight: 600; }
  .info-ingredients { left: 43px; top: 51px; width: 260px; }
  .info-best { left: 43px; top: 110px; width: 250px; }
  .info-volume { left: 43px; top: 178px; }
  .info-storage { left: 43px; top: 217px; width: 230px; }
  .info-address { left: 43px; top: 289px; }
  .divider { position: absolute; width: 48px; height: 8px; }
  .maker-mark {
    position: absolute; left: 246px; top: 287px; width: 86px;
    font-size: 10px; font-weight: 600; color: var(--brown);
    text-align: center; line-height: 12px;
    display: flex; flex-direction: column; align-items: center; gap: 5px;
  }
  .maker-mark .dot { width: 24px; height: 24px; background: var(--brown); border-radius: 3px; }
  .names {
    position: absolute; left: 330px; top: 44px; width: 320px; margin: 0;
    text-align: center; font-family: "Great Vibes", cursive; font-weight: 400;
    color: var(--brown); line-height: 1;
  }
  .names .groom { font-size: 40px; display: block; }
  .names .amp { font-size: 30px; display: block; margin: -2px 0; }
  .names .bride { font-size: 46px; display: block; }
  .heart-rule { position: absolute; left: 461px; top: 162px; width: 62px; height: 14px; }
  .date {
    position: absolute; left: 400px; top: 180px; width: 180px;
    display: flex; justify-content: center; align-items: center;
    font-family: "Kaushan Script", cursive; color: var(--brown);
  }
  .date span { padding: 0 8px; }
  .date .month, .date .year { font-size: 12px; }
  .date .day { font-size: 18px; border-left: 1px solid var(--brown); border-right: 1px solid var(--brown); padding: 2px 8px; }
  .style-name {
    position: absolute; left: 390px; top: 380px; width: 200px; margin: 0; text-align: center;
    font-family: "Kaushan Script", cursive; font-size: 15px; color: var(--brown);
  }
  .story {
    position: absolute; left: 709px; top: 51px; width: 240px; margin: 0;
    font-size: 12.5px; line-height: 17.5px; text-align: justify;
  }
  .badges { position: absolute; left: 688px; top: 214px; display: flex; gap: 8px; }
  .badge {
    width: 44px; height: 44px; border-radius: 50%;
    border: 1.5px solid var(--brown); box-shadow: inset 0 0 0 2.5px var(--cream), inset 0 0 0 3.5px var(--brown);
    display: flex; flex-direction: column; align-items: center; justify-content: center;
    font-size: 6.5px; line-height: 9px; color: var(--text);
  }
  .badge strong { font-size: 8px; font-weight: 700; }
  .contacts { position: absolute; left: 709px; top: 300px; font-size: 12.5px; line-height: 22px; }
  .contacts .social { display: flex; align-items: center; gap: 8px; padding-left: 18px; }
  .contacts .sq { width: 11px; height: 11px; background: var(--text); border-radius: 2px; }
  .contacts b { font-weight: 600; }
</style>
</head>
<body>
  <section class="label">
    <div class="art sprig-left" role="img" aria-label="faint leafy sprig decoration"></div>
    <div class="art sprig-right" role="img" aria-label="faint leafy sprig decoration"></div>
    <svg class="wreath-arcs" viewBox="0 0 985 414" aria-hidden="true">
      <path d="M421 0C370 30 338 80 332 150C328 200 340 240 360 270" fill="none" stroke="var(--line)" stroke-width="1.2"/>
      <path d="M570 0C600 20 625 45 640 80" fill="none" stroke="var(--line)" stroke-width="1.2"/>
    </svg>
    <div class="art leaves-left" role="img" aria-label="leafy branch decoration"></div>
    <div class="art leaves-right" role="img" aria-label="leafy branch decoration"></div>

    <p class="info info-ingredients"><b>Lista składników</b>: woda, słód jęczmienny, chmiel, liście limonki, drożdże.</p>
    <svg class="divider" style="left:108px;top:94px" viewBox="0 0 48 8" aria-hidden="true"><path d="M0 4H48" stroke="#6b4a2e" stroke-width="1"/></svg>
    <p class="info info-best"><b>Najlepiej spożyć przed:</b><br>Data stanowi numer partii</p>
    <p class="info info-volume"><b>VOLUME OF THE BOTTLE:</b> 330ml</p>
    <svg class="divider" style="left:108px;top:204px" viewBox="0 0 48 8" aria-hidden="true"><path d="M0 4H48" stroke="#6b4a2e" stroke-width="1"/></svg>
    <p class="info info-storage"><b>STORAGE CONDITIONS:</b><br>Przechowywać w suchym i ciemnym miejscu</p>
    <svg class="divider" style="left:108px;top:276px" viewBox="0 0 48 8" aria-hidden="true"><path d="M0 4H48" stroke="#6b4a2e" stroke-width="1"/></svg>
    <p class="info info-address">Wytwórnia Orlik<br>34-100 Górna Dolina<br>Browar Klasztorny Dąb<br>Zielonka 12, 34-600 Zielonka</p>
    <div class="maker-mark"><span class="dot"></span><span>Wytwórnia Orlik</span></div>

    <h1 class="names">
      <span class="groom">Jan Kowal</span>
      <span class="amp">&amp;</span>
      <span class="bride">Zofia Maja</span>
    </h1>
    <svg class="heart-rule" viewBox="0 0 62 14" aria-hidden="true"><path d="M0 12H62" stroke="#6b4a2e" stroke-width="1"/></svg>
    <div class="date"><span class="month">Nov</span><span class="day">05</span><span class="year">2020</span></div>
    <div class="art couple" role="img" aria-label="sketch of an embracing bride and groom"></div>
    <p class="style-name">India Pale Ale</p>

    <p class="story">Trzymasz w ręku naszą autorską IPA do produkcji której wykorzystujemy wodę wypływającą z samego serca Beskidu Wysokiego – Babiej Góry. IPA lubi chmiele i goryczkę, ale żeby nie było nudno postanowiliśmy ją wzbogacić limonką.</p>
    <svg class="divider" style="left:826px;top:190px" viewBox="0 0 48 8" aria-hidden="true"><path d="M0 4H48" stroke="#6b4a2e" stroke-width="1"/></svg>
    <div class="badges">
      <div class="badge">ALK<strong>5%</strong></div>
      <div class="badge">IBU<strong>MEDIUM</strong></div>
      <div class="badge">EBC<strong>PALE</strong></div>
      <div class="badge">EXT<strong>14%</strong></div>
      <div class="badge">WATER
        <svg width="22" height="10" viewBox="0 0 22 10" aria-hidden="true"><path d="M1 9L8 2L12 6L15 3L21 9Z" fill="#6b4a2e"/></svg>
      </div>
    </div>
    <svg class="divider" style="left:826px;top:280px" viewBox="0 0 48 8" aria-hidden="true"><path d="M0 4H48" stroke="#6b4a2e" stroke-width="1"/></svg>
    <div class="contacts">
      <div class="social"><span class="sq"></span>– worlik</div>
      <div class="social"><span class="sq"></span>– wytworniaorlik</div>
      <div><b>WEBSITE</b> – www.wytworniaorlik.pl</div>
    </div>
  </section>
</body>
</html>
```